Lumen Ridge Puzzles Business Cards
Two-sided business cards
Professional
Pim Varlotte
Founder, KORV Fellow, Brellaquin MVP
pim@lumenridgepuzzles.example
www.lumenridgepuzzles.example
GPG Fingerprint: A2D1 5B09 F6C3 17E4 8D2A 40BC 9E71 3F58 C046
Logo to Use for Business Cards

```html
<!DOCTYPE html>
<html lang="en">
<head>
<meta charset="utf-8">
<title>Lumen Ridge Puzzles – Business Card</title>
<link rel="stylesheet" href="https://fonts.googleapis.com/css2?family=Arimo:wght@400;700&display=swap">
<style>
  :root {
    --page-bg: #ece9e4;
    --card-black: #050505;
    --brand-blue: #2f8fd8;
    --brand-blue-deep: #1a3f9c;
    --brand-blue-bright: #3aa0e8;
    --accent-green: #8cc63f;
    --text-white: #ffffff;
  }
  html, body {
    margin: 0;
    padding: 0;
    width: 1200px;
    height: 935px;
    overflow: hidden;
    background: var(--page-bg);
    font-family: "Arimo", Arial, sans-serif;
  }
  .business-card {
    position: absolute;
    left: 150px;
    top: 210px;
    width: 900px;
    height: 514px;
    background: var(--card-black);
    border-radius: 34px;
    overflow: hidden;
    box-shadow: 0 10px 24px rgba(0,0,0,0.25);
  }
  .brand-block {
    position: absolute;
    left: 0;
    right: 0;
    top: 26px;
    text-align: center;
  }
  .brand-mark {
    display: block;
    margin: 0 auto;
  }
  .brand-name {
    margin: 16px 0 0;
    font-weight: 700;
    font-size: 40px;
    letter-spacing: 2px;
    text-transform: uppercase;
    color: var(--brand-blue);
  }
  .person {
    position: absolute;
    left: 56px;
    top: 318px;
    width: 290px;
  }
  .person-name {
    margin: 0;
    font-size: 28px;
    font-weight: 400;
    color: var(--brand-blue-bright);
  }
  .person-title {
    margin: 6px 0 0;
    font-size: 21px;
    line-height: 27px;
    color: var(--text-white);
  }
  .divider {
    position: absolute;
    left: 366px;
    top: 300px;
    width: 3px;
    height: 136px;
    background: linear-gradient(to bottom, var(--accent-green), var(--brand-blue));
  }
  .contact-list {
    position: absolute;
    left: 388px;
    top: 300px;
    margin: 0;
    padding: 0;
    list-style: none;
    font-size: 22px;
    line-height: 33px;
    color: var(--text-white);
  }
  .contact-label {
    color: var(--brand-blue-bright);
    font-weight: 700;
  }
  .fingerprint-continued {
    padding-left: 66px;
  }
  .base-stripe {
    position: absolute;
    left: 0;
    right: 0;
    top: 454px;
    height: 6px;
    background: var(--accent-green);
  }
  .base-band {
    position: absolute;
    left: 0;
    right: 0;
    top: 462px;
    bottom: 0;
    background: linear-gradient(to right, var(--brand-blue-deep), var(--brand-blue-bright) 55%, var(--brand-blue-deep));
  }
</style>
</head>
<body>
  <div class="business-card">
    <div class="brand-block">
      <svg class="brand-mark" width="160" height="160" viewBox="0 0 160 160" aria-hidden="true">
        <circle cx="80" cy="80" r="76" fill="#2f8fd8"/>
      </svg>
      <p class="brand-name">Lumen Ridge Puzzles</p>
    </div>

    <div class="person">
      <p class="person-name">Pim Varlotte</p>
      <p class="person-title">Founder, KORV Fellow,<br>Brellaquin MVP</p>
    </div>

    <div class="divider"></div>

    <ul class="contact-list">
      <li><span class="contact-label">E :</span> pim@lumenridgepuzzles.example</li>
      <li><span class="contact-label">W :</span> www.lumenridgepuzzles.example</li>
      <li><span class="contact-label">GPG :</span> A2D1 5B09 F6C3 17E4 8D2A</li>
      <li class="fingerprint-continued">40BC 9E71 3F58 C046</li>
    </ul>

    <div class="base-stripe"></div>
    <div class="base-band"></div>
  </div>
</body>
</html>
```